Cover Art Needed For Digital Single Release

We are looking to have the cover art designed for a new song called "Paper Lanterns". You will find the track attached below in a private Tunepool link so that you can have a listen.
We are thinking of keeping the artwork fairly simple but still want it to catch your eye. Maybe using the song title and artist’s name in a colorful and creative way. (A well-designed font with a bold color scheme, or even something like a mosaic style art piece featuring the title).
We completely welcome any and all creative visions you might have, even if it strays away from the examples given above.
Thank you in advance for your submissions, and we are excited to collaborate with you!
"Paper Lanterns" by Marcus Fell
https://tunepool.example/marcuszxq/paper-lanterns/s-r7tWnexiLqa
Target Market(s)
Teens/Young Adults
Industry/Entity Type
Music
Requirements
Must have
- An eye-catching design
Should not have
- Please do not rely heavily on stock images. We prefer an original design/concept.

```html
<!DOCTYPE html>
<html lang="en">
<head>
<meta charset="utf-8">
<title>Marcus Fell – Paper Lanterns</title>
<link rel="stylesheet" href="https://fonts.googleapis.com/css2?family=Archivo+Black&family=Montserrat:wght@600;700;800&family=Staatliches&display=swap">
<style>
  :root{
    --paper:#e9e1d3;
    --paper-light:#f2ede4;
    --paper-shade:#cfc3b0;
    --ink:#3b3734;
    --ink-soft:#6f6962;
    --red:#c9402b;
    --orange:#e0a23a;
    --orange-deep:#b8741f;
    --purple:#a98bc4;
    --tan:#b8955a;
    --peach:#f7d9b4;
    --byline:#c9402b;
    --title:#2b2a2c;
  }
  html,body{margin:0;padding:0;width:1200px;height:1200px;overflow:hidden;background:#fff}
  .cover{position:relative;width:1200px;height:1200px;background:var(--paper);overflow:hidden}
  .collage{position:absolute;inset:0;width:1200px;height:1200px}
  .word-heavy{font-family:"Archivo Black",sans-serif}
  .word-stencil{font-family:"Staatliches",sans-serif}
  .outline-red{fill:none;stroke:var(--red);stroke-width:7}
  .credit{
    position:absolute;left:98px;top:1098px;
    display:flex;align-items:baseline;gap:14px;
    font-family:"Montserrat",sans-serif;
  }
  .credit-artist{color:var(--byline);font-weight:800;font-size:32px;letter-spacing:.95em;text-transform:uppercase}
  .credit-title{color:var(--title);font-weight:700;font-size:38px;letter-spacing:-.01em}
</style>
</head>
<body>
<main class="cover">
  <svg class="collage" viewBox="0 0 1200 1200" xmlns="http://www.w3.org/2000/svg">
    <!-- top-left outlined fragment -->
    <text class="word-heavy outline-red" x="-60" y="165" font-size="210" letter-spacing="30">PER</text>

    <!-- large grey background word -->
    <text class="word-heavy" x="190" y="430" font-size="270" fill="var(--ink-soft)" opacity=".75">lan</text>

    <!-- top-right torn slip -->
    <g transform="rotate(18 900 170)">
      <polygon points="620,70 1175,60 1185,250 640,275" fill="var(--paper-light)"/>
      <text class="word-heavy" x="640" y="220" font-size="106" fill="var(--orange)" stroke="var(--orange-deep)" stroke-width="2" textLength="520">LANTERNS</text>
    </g>

    <!-- purple backing strip -->
    <polygon points="130,560 1120,470 1140,600 180,760" fill="var(--purple)"/>

    <!-- central outlined word on paper strips -->
    <polygon points="155,440 1090,370 1130,550 175,610" fill="var(--paper-light)"/>
    <text class="word-heavy outline-red" x="195" y="565" font-size="170" textLength="880" transform="rotate(-4 600 500)">PAPER</text>

    <!-- left edge fragments -->
    <text class="word-heavy" x="-20" y="660" font-size="220" fill="var(--orange)">E</text>
    <text class="word-heavy" x="-40" y="1040" font-size="230" fill="var(--orange)">IN</text>

    <!-- tan backing and peach fragment -->
    <polygon points="330,860 980,770 1020,890 380,985" fill="var(--tan)"/>
    <text class="word-heavy" x="395" y="975" font-size="130" fill="var(--peach)">la</text>

    <!-- main lowercase word on white slip -->
    <g transform="rotate(-3 700 780)">
      <polygon points="360,690 1050,660 1060,850 380,880" fill="var(--paper-light)"/>
      <text class="word-heavy" x="385" y="835" font-size="128" fill="var(--ink-soft)" textLength="645">lanterns</text>
    </g>

    <!-- stencil word -->
    <text class="word-stencil" x="680" y="1090" font-size="120" fill="var(--red)" opacity=".85" textLength="445">LANTERNS</text>
  </svg>

  <div class="credit">
    <span class="credit-artist">Marcus Fell</span>
    <span class="credit-title">paper lanterns</span>
  </div>
</main>
</body>
</html>
```